For Lease sign for Property management company in Kansas City

We need someone to take our information and design a standard for lease sign that we can put in front of each of our buildings. I would love for it to do its job of letting people know there are units available but also be unique somehow. Also the aspect ratio of the design would ideally be 4 wide by 3 tall but we open to other ideas. It will be a larger yard sign.

Target Market(s)

Potential Tenants

Industry/Entity Type

Real Estate Development

Font styles to use
Sans Serif

Requirements
Must have
• Our logo, our website (www.quillstead-properties.com), our phone number (816) 555-2719.
Nice to have
• Some how say "For Lease"
Sign to be 4' wide by 3' tall
If there was a place to put the building name that would be cool but not ne
Should not have
• Nothing that I can think of

```html
<!DOCTYPE html>
<html lang="en">
<head>
<meta charset="utf-8">
<title>For Lease – Quillstead Properties</title>
<link rel="stylesheet" href="https://fonts.googleapis.com/css2?family=Montserrat:wght@800&display=swap">
<style>
  :root {
    --sign-red: #BE1E2D;
    --sign-gold: #FBB042;
    --sign-gold-rim: #D9973A;
    --sign-white: #FFFFFF;
  }
  html, body {
    margin: 0;
    padding: 0;
    width: 1200px;
    height: 900px;
    overflow: hidden;
    background: var(--sign-red);
  }
  .lease-sign {
    display: block;
    width: 1200px;
    height: 900px;
    font-family: "Montserrat", Arial, sans-serif;
    font-weight: 800;
  }
  .sign-field { fill: var(--sign-red); }
  .center-band { fill: var(--sign-white); }
  .brand-disc { fill: var(--sign-gold); stroke: var(--sign-gold-rim); stroke-width: 8; }
  .headline { fill: var(--sign-gold); font-size: 162px; }
  .brand-name { fill: var(--sign-red); font-size: 52px; }
  .phone-number { fill: var(--sign-white); font-size: 110px; }
  .web-address { fill: var(--sign-gold); font-size: 58px; }
</style>
</head>
<body>
<svg class="lease-sign" viewBox="0 0 1200 900" xmlns="http://www.w3.org/2000/svg">
  <rect class="sign-field" x="0" y="0" width="1200" height="900"/>
  <polygon class="center-band" points="0,343 600,432 1200,343 1200,557 600,476 0,557"/>

  <text class="headline" x="118" y="179" textLength="964" lengthAdjust="spacingAndGlyphs">FOR LEASE</text>

  <g class="brand-mark">
    <circle class="brand-disc" cx="600" cy="450" r="217"/>
    <text class="brand-name" x="600" y="469" text-anchor="middle" textLength="330" lengthAdjust="spacingAndGlyphs">QUILLSTEAD</text>
  </g>

  <text class="phone-number" x="157" y="781" textLength="885" lengthAdjust="spacingAndGlyphs">(816) 555-2719</text>
  <text class="web-address" x="82" y="858" textLength="1036" lengthAdjust="spacingAndGlyphs">WWW.QUILLSTEAD-PROPERTIES.COM</text>
</svg>
</body>
</html>
```